Real Estate Listing Landing Page

I am looking for a landing page for my Flat Fee MLS Listing website... The name of my website is "Brightkey Home Sales".

I am a big fan of this landing page setup and would like something similar.
https://quaylinehomes.com/

I am a fan of the design style on https://quaylinehomes.com/ and also this design style as well... https://2817.velmontedge.com/

Use your creativity and incorporate your own twists that you would feel lift up this landing pages' appeal. I'd love some red color incorporated within the design.

Target Market(s)

Real Estate Home Sellers

Industry/Entity Type

Real Estate

Coding

Coded - Design and coding required

Font styles to use
Sans Serif

Colors
0054AA
0677BA
7BADD7
CADEEF
E8F1F8
0094D4
00A9DD
6FCCEA
C7EBF8
E9F6FB
EB3D1F
EC4F4E
F09395
F8D3D4
FCEDEE

```html
<!DOCTYPE html>
<html lang="en">
<head>
<meta charset="utf-8">
<title>Brightkey Home Sales – Landing Page</title>
<link href="https://fonts.googleapis.com/css2?family=Poppins:wght@300;400;500;600;700&display=swap" rel="stylesheet">
<style>
:root{
  --stage:#7d7d7d;
  --white:#ffffff;
  --ink:#141414;
  --muted:#8a8a8a;
  --red:#d90f0f;
  --red-deep:#c40808;
  --pink:#f8d3d4;
  --pink-soft:#fcedee;
  --pink-num:#f09395;
  --grey-block:#ececec;
  --grey-field:#f1f1f1;
}
*{box-sizing:border-box;margin:0;padding:0}
html,body{width:1200px;height:3532px;overflow:hidden}
body{background:var(--stage);font-family:"Poppins",Arial,sans-serif;color:var(--ink);position:relative}
.abs{position:absolute}
.screen{position:absolute;background:var(--white);overflow:hidden}
.screen--desktop{left:72px;top:32px;width:728px;height:3456px}
.screen--mobile{left:824px;top:32px;width:348px;height:3456px}

/* shared */
.logo{font-weight:700;color:var(--ink);letter-spacing:-.2px}
.btn-red{position:absolute;background:var(--red);color:var(--white);font-weight:500;display:flex;align-items:center;justify-content:center}
.btn-outline{position:absolute;border:2px solid var(--red);color:var(--red);background:var(--white);font-weight:500;display:flex;align-items:center;justify-content:center;letter-spacing:.5px}
.photo{position:absolute}
.photo--interior{background:linear-gradient(135deg,#d8c2a6 0%,#a47c58 40%,#6e5443 70%,#c9b49a 100%)}
.photo--building{background:linear-gradient(160deg,#f4f4f4 0%,#d9dadc 45%,#b6b9bd 75%,#eceded 100%)}
.photo--fern{background:linear-gradient(160deg,#1f5e1c 0%,#3c8a2e 45%,#174a15 100%)}
.tag-box{position:absolute;background:var(--red);color:var(--white);font-size:9px;font-weight:600;letter-spacing:.5px;text-align:center;display:flex;align-items:flex-end;justify-content:center;padding:0 6px 12px;line-height:1.3}
.arrows{position:absolute;display:flex;gap:22px}
.arrows svg{width:22px;height:14px}
.vertical{position:absolute;writing-mode:vertical-rl;transform:rotate(180deg);white-space:nowrap}
.big-num{position:absolute;writing-mode:vertical-rl;transform:rotate(180deg);font-weight:700;color:var(--pink-num);opacity:.7;line-height:1}
.side-label{font-size:11px;color:var(--muted);letter-spacing:1px}
.side-label b{display:inline-block;width:1px;height:44px;background:var(--muted);margin:8px 0;vertical-align:middle}
.red{color:var(--red)}
.field{background:var(--grey-field);font-size:11px;color:#9a9a9a;padding:0 14px;display:flex;align-items:center}

/* desktop */
.d-topbar{position:absolute;top:28px;right:36px;display:flex;gap:18px;font-size:10px;color:var(--red)}
.d-logo{position:absolute;left:64px;top:90px;font-size:22px}
.d-nav{position:absolute;top:90px;right:36px;display:flex;gap:28px;align-items:center;font-size:12px;color:#444}
.d-nav .contact{border:1.5px solid var(--red);color:var(--red);padding:6px 16px}
.d-hero-kicker{left:68px;top:244px;font-size:12px;letter-spacing:2px;color:var(--muted)}
.d-hero-title{left:64px;top:264px;font-size:58px;font-weight:700;line-height:1.02;letter-spacing:-1px}
.d-social{left:68px;top:596px;display:flex;gap:22px;font-size:11px;color:var(--muted)}
.d-heading{font-size:40px;font-weight:400;line-height:1.18;letter-spacing:-.5px}

/* mobile */
.m-logo{position:absolute;left:14px;top:28px;font-size:22px;line-height:1.15}
.m-burger{position:absolute;right:14px;top:36px;width:30px;height:30px}
.m-title{left:14px;top:160px;font-size:50px;font-weight:700;line-height:1.02;letter-spacing:-1px}
.m-heading{font-size:42px;font-weight:400;line-height:1.12;letter-spacing:-.5px}
.m-copy{font-size:15px;line-height:1.6;color:#555}
</style>
</head>
<body>

<!-- ========== DESKTOP ========== -->
<section class="screen screen--desktop" aria-label="Desktop landing page">
  <div class="d-topbar"><span>555-014-2286</span><span>hello@brightkeyhomes.com</span></div>
  <div class="logo d-logo">Brightkey Home Sales</div>
  <nav class="d-nav"><span>Search</span><span>Properties</span><span>About Us</span><span class="contact">Contact</span></nav>

  <!-- hero -->
  <div class="photo photo--building" style="left:308px;top:128px;width:420px;height:540px" role="img" aria-label="White modern condominium tower with stacked balconies"></div>
  <div class="vertical side-label" style="left:20px;top:260px">01 <b></b> 04</div>
  <p class="abs d-hero-kicker">HARBORLINE AVE</p>
  <h1 class="abs d-hero-title">Live the dream.<br>Modern Condos</h1>
  <div class="btn-red" style="left:64px;top:420px;width:120px;height:40px;font-size:12px">View Listing</div>
  <div class="abs d-social"><span>Feedwall</span><span>Pixelroll</span></div>
  <div class="arrows" style="left:636px;top:556px">
    <svg viewBox="0 0 22 14"><path d="M21 7H2M8 1L2 7l6 6" fill="none" stroke="#d90f0f" stroke-width="2"/></svg>
    <svg viewBox="0 0 22 14"><path d="M1 7h19M14 1l6 6-6 6" fill="none" stroke="#d90f0f" stroke-width="2"/></svg>
  </div>

  <!-- 001 buyers -->
  <div class="abs" style="left:188px;top:708px;width:440px;height:250px;background:var(--grey-block)"></div>
  <div class="vertical side-label" style="left:20px;top:720px">Buyers <b></b> 001.</div>
  <div class="big-num" style="left:62px;top:712px;font-size:84px">001.</div>
  <p class="abs" style="left:300px;top:768px;width:300px;text-align:right;font-size:18px;line-height:1.25"><strong style="font-weight:600">Looking to buy?</strong><br>We have some of the best<br>properties</p>
  <div class="photo photo--interior" style="left:8px;top:856px;width:620px;height:340px" role="img" aria-label="Bright living room with sofa, coffee table and wood floors"></div>
  <div class="tag-box" style="left:536px;top:888px;width:80px;height:88px">VIEW<br>PROPERTIES</div>
  <div class="abs" style="left:8px;top:1196px;width:240px;height:12px;background:var(--red)"></div>
  <div class="arrows" style="left:508px;top:1168px">
    <svg viewBox="0 0 22 14"><path d="M21 7H2M8 1L2 7l6 6" fill="none" stroke="#d90f0f" stroke-width="2"/></svg>
    <svg viewBox="0 0 22 14"><path d="M1 7h19M14 1l6 6-6 6" fill="none" stroke="#d90f0f" stroke-width="2"/></svg>
  </div>

  <!-- 002 locations -->
  <div class="abs" style="left:168px;top:1250px;width:560px;height:420px;background:var(--pink-soft)"></div>
  <div class="vertical side-label" style="left:20px;top:1370px">Locations <b></b> 002.</div>
  <div class="big-num" style="left:62px;top:1400px;font-size:84px">002.</div>
  <div class="photo photo--building" style="left:68px;top:1288px;width:280px;height:560px" role="img" aria-label="Angled white apartment building facade against pale sky"></div>
  <h2 class="abs d-heading" style="left:372px;top:1316px">Spaces that<br>make<br>a difference.<br><span class="red">Browse our</span></h2>
  <div class="btn-red" style="left:416px;top:1548px;width:240px;height:72px;font-size:26px;gap:18px">Properties
    <svg width="26" height="14" viewBox="0 0 26 14"><path d="M1 7h23M18 1l6 6-6 6" fill="none" stroke="#fff" stroke-width="2"/></svg></div>
  <div class="photo photo--interior" style="left:376px;top:1672px;width:340px;height:212px" role="img" aria-label="Open-plan kitchen and dining area"></div>
  <div class="tag-box" style="left:328px;top:1700px;width:80px;height:88px">VIEW<br>RENTALS</div>

  <!-- 003 rentals -->
  <div class="abs" style="left:0;top:2256px;width:600px;height:210px;background:var(--grey-block)"></div>
  <div class="vertical side-label" style="left:20px;top:2130px">Rentals <b></b> 003.</div>
  <div class="big-num" style="left:62px;top:2050px;font-size:84px">003.</div>
  <h2 class="abs d-heading" style="left:360px;top:2108px">We Offer<br><span style="display:inline-block;width:46px;height:3px;background:var(--ink);vertical-align:middle;margin-right:14px"></span>Rental Services</h2>
  <p class="abs" style="left:148px;top:2210px;width:210px;font-size:9px;line-height:1.6;color:#666">A wonderful serenity has taken possession of my entire soul, like these sweet mornings of spring which I enjoy with my whole heart. I am alone, and feel the charm of existence in this spot, which was created for the bliss of souls like mine.</p>
  <div class="photo photo--interior" style="left:88px;top:2328px;width:528px;height:320px" role="img" aria-label="Furnished living room with grey sofa and rug"></div>
  <div class="tag-box" style="left:528px;top:2328px;width:80px;height:88px">VIEW<br>PROPERTIES</div>
  <div class="arrows" style="left:508px;top:2612px">
    <svg viewBox="0 0 22 14"><path d="M21 7H2M8 1L2 7l6 6" fill="none" stroke="#d90f0f" stroke-width="2"/></svg>
    <svg viewBox="0 0 22 14"><path d="M1 7h19M14 1l6 6-6 6" fill="none" stroke="#d90f0f" stroke-width="2"/></svg>
  </div>

  <!-- contact -->
  <div class="abs" style="left:8px;top:2744px;width:520px;height:420px;background:var(--grey-block)"></div>
  <div class="photo photo--fern" style="left:536px;top:2728px;width:192px;height:632px" role="img" aria-label="Close-up of green fern leaves"></div>
  <form class="abs" style="left:108px;top:2788px;width:380px;height:400px;background:var(--white);box-shadow:0 6px 24px rgba(0,0,0,.12);padding:26px 24px">
    <h3 style="font-size:20px;font-weight:500;margin-bottom:10px">Contact Us</h3>
    <p style="font-size:10px;line-height:1.5;color:#666;margin-bottom:14px">Please complete this form if you would like to have more information on any of our properties.</p>
    <div class="field" style="height:34px;margin-bottom:8px">Full Name</div>
    <div class="field" style="height:34px;margin-bottom:8px">Email</div>
    <div class="field" style="height:34px;margin-bottom:8px">Phone</div>
    <div class="field" style="height:56px;align-items:flex-start;padding-top:10px;margin-bottom:14px">Additional Notes</div>
    <div style="background:var(--red);color:#fff;height:40px;display:flex;align-items:center;justify-content:center;font-size:11px;font-weight:500">Submit Request</div>
  </form>

  <footer class="abs" style="left:0;top:3360px;width:728px;height:96px;background:var(--red);color:#fff;display:flex;align-items:center;padding:0 64px">
    <span style="font-size:20px;font-weight:700">Brightkey Home Sales</span>
    <span style="margin-left:40px;font-size:10px;display:flex;gap:22px"><span>Feedwall</span><span>Pixelroll</span></span>
    <span style="margin-left:auto;font-size:10px;display:flex;gap:22px"><span>555-014-2286</span><span>hello@brightkeyhomes.com</span></span>
  </footer>
</section>

<!-- ========== MOBILE ========== -->
<section class="screen screen--mobile" aria-label="Mobile landing page">
  <div class="logo m-logo">Brightkey<br>Home Sales</div>
  <svg class="m-burger" viewBox="0 0 30 30"><circle cx="15" cy="15" r="14" fill="none" stroke="#d90f0f" stroke-width="1.5"/><path d="M9 11h12M9 15h12M9 19h12" stroke="#d90f0f" stroke-width="1.5"/></svg>

  <div class="photo photo--building" style="left:176px;top:128px;width:172px;height:340px" role="img" aria-label="White modern condominium tower"></div>
  <p class="abs" style="left:16px;top:138px;font-size:12px;letter-spacing:2px;color:var(--muted)">HARBORLINE AVE</p>
  <h1 class="abs m-title">Live the<br>dream.<br>Modern<br>Condos</h1>
  <div class="btn-red" style="left:24px;top:368px;width:264px;height:56px;font-size:15px">View Listing</div>
  <div class="arrows" style="left:254px;top:476px">
    <svg viewBox="0 0 22 14"><path d="M21 7H2M8 1L2 7l6 6" fill="none" stroke="#d90f0f" stroke-width="2"/></svg>
    <svg viewBox="0 0 22 14"><path d="M1 7h19M14 1l6 6-6 6" fill="none" stroke="#d90f0f" stroke-width="2"/></svg>
  </div>

  <div class="abs" style="left:0;top:568px;width:348px;height:300px;background:var(--pink-soft)"></div>
  <p class="abs" style="left:40px;top:600px;width:296px;text-align:right;font-size:19px;line-height:1.25"><strong style="font-weight:600">Looking to buy?</strong><br>We have some of the best<br>properties</p>
  <div class="btn-outline" style="left:16px;top:716px;width:300px;height:56px;font-size:14px">VIEW PROPERTIES</div>
  <div class="photo photo--interior" style="left:16px;top:800px;width:300px;height:148px" role="img" aria-label="Bright living room interior"></div>
  <div class="arrows" style="left:254px;top:958px">
    <svg viewBox="0 0 22 14"><path d="M21 7H2M8 1L2 7l6 6" fill="none" stroke="#d90f0f" stroke-width="2"/></svg>
    <svg viewBox="0 0 22 14"><path d="M1 7h19M14 1l6 6-6 6" fill="none" stroke="#d90f0f" stroke-width="2"/></svg>
  </div>

  <div class="abs" style="left:0;top:1000px;width:348px;height:380px;background:var(--pink)"></div>
  <h2 class="abs m-heading" style="left:16px;top:1030px">Spaces that<br>make<br>a difference.<br><span class="red">Find them in</span></h2>
  <div class="btn-red" style="left:16px;top:1260px;width:260px;height:80px;font-size:32px;gap:18px">Westgate
    <svg width="26" height="14" viewBox="0 0 26 14"><path d="M1 7h23M18 1l6 6-6 6" fill="none" stroke="#fff" stroke-width="2"/></svg></div>

  <h2 class="abs m-heading" style="left:16px;top:1420px">We Offer<br><span style="display:inline-block;width:40px;height:3px;background:var(--ink);vertical-align:middle;margin-right:12px"></span>Rental<br>Services</h2>
  <p class="abs m-copy" style="left:16px;top:1604px;width:310px">A wonderful serenity has taken possession of my entire soul, like these sweet mornings of spring which I enjoy with my whole heart. I am alone, and feel the charm of existence in this spot, which was created for the bliss of souls like mine.</p>
  <div class="btn-outline" style="left:16px;top:1840px;width:300px;height:56px;font-size:14px">VIEW RENTALS</div>
  <div class="photo photo--interior" style="left:16px;top:1920px;width:300px;height:148px" role="img" aria-label="Furnished rental living room"></div>
  <div class="arrows" style="left:254px;top:2078px">
    <svg viewBox="0 0 22 14"><path d="M21 7H2M8 1L2 7l6 6" fill="none" stroke="#d90f0f" stroke-width="2"/></svg>
    <svg viewBox="0 0 22 14"><path d="M1 7h19M14 1l6 6-6 6" fill="none" stroke="#d90f0f" stroke-width="2"/></svg>
  </div>

  <div class="abs" style="left:0;top:2140px;width:348px;height:680px;background:var(--grey-block)"></div>
  <form class="abs" style="left:16px;top:2148px;width:316px;height:640px;background:var(--white);padding:28px 20px">
    <h3 style="font-size:26px;font-weight:500;margin-bottom:14px">Contact Us</h3>
    <p class="m-copy" style="margin-bottom:22px">Please complete this form if you would like to have more information on any of our properties.</p>
    <div class="field" style="height:52px;margin-bottom:14px;font-size:13px">Full Name</div>
    <div class="field" style="height:52px;margin-bottom:14px;font-size:13px">Email</div>
    <div class="field" style="height:52px;margin-bottom:14px;font-size:13px">Phone</div>
    <div class="field" style="height:96px;align-items:flex-start;padding-top:14px;margin-bottom:26px;font-size:13px">Additional Notes</div>
    <div style="background:var(--red);color:#fff;height:60px;display:flex;align-items:center;justify-content:center;font-size:15px;font-weight:500">Submit Request</div>
  </form>

  <footer class="abs" style="left:0;top:2840px;width:348px;height:616px;background:var(--red);color:#fff;padding:48px 16px">
    <div style="font-size:26px;font-weight:700;line-height:1.2;margin-bottom:40px">Brightkey<br>Home Sales</div>
    <p style="font-size:13px;line-height:2">555-014-2286<br>hello@brightkeyhomes.com</p>
    <p style="font-size:13px;line-height:2;margin-top:16px">Feedwall<br>Pixelroll</p>
  </footer>
</section>

</body>
</html>
```